HomeBridle business card and stationary design

We are looking for a simple yet elegant design for our mortgage company business card and stationary.

The card should include:
Name (Derek Walsh)
Title (CEO)
Phone Number (614-208-3917)
Address (48 Birchfield Court, Suite 314, Marlow, OH 43952)
Email (email@homebridle-example.com)
"NMLS" i.e. (NMLS 61947)
"Company NMLS" (Company NMLS 472815)

See above

```html
<!DOCTYPE html>
<html lang="en">
<head>
<meta charset="utf-8">
<title>HomeBridle Business Card</title>
<link href="https://fonts.googleapis.com/css2?family=Montserrat:wght@400;500;600&display=swap" rel="stylesheet">
<style>
  :root {
    --backdrop: #f3f2f1;
    --card-white: #f7f7f7;
    --card-navy: #1c2733;
    --brand-blue: #29a3dc;
    --ink: #1e2a36;
    --text-grey: #5a6068;
    --shadow: rgba(20, 30, 40, 0.14);
  }
  * { box-sizing: border-box; margin: 0; padding: 0; }
  html, body {
    width: 1200px;
    height: 800px;
    overflow: hidden;
    background: var(--backdrop);
    font-family: "Montserrat", Arial, sans-serif;
  }
  .stage {
    position: relative;
    width: 1200px;
    height: 800px;
  }
  .card {
    position: absolute;
    top: 246px;
    width: 540px;
    height: 308px;
    border-radius: 3px;
    box-shadow: 0 10px 28px var(--shadow);
  }
  .card--front { left: 40px; background: var(--card-white); }
  .card--back  { left: 620px; background: var(--card-navy); }

  .wordmark {
    font-weight: 600;
    letter-spacing: -0.5px;
    display: flex;
    align-items: center;
    gap: 10px;
  }
  .wordmark__dot {
    width: 12px;
    height: 12px;
    border-radius: 50%;
    background: var(--brand-blue);
  }
  .card--front .wordmark {
    position: absolute;
    left: 52px;
    top: 46px;
    font-size: 34px;
    color: var(--ink);
  }
  .card--back .wordmark {
    position: absolute;
    left: 0; right: 0; top: 0; bottom: 0;
    justify-content: center;
    font-size: 46px;
    color: var(--brand-blue);
  }

  .licence {
    position: absolute;
    left: 28px;
    top: 150px;
    padding-left: 16px;
    border-left: 2px solid var(--ink);
    font-size: 11.5px;
    line-height: 1.6;
    color: var(--text-grey);
  }

  .contact {
    position: absolute;
    left: 292px;
    top: 138px;
    color: var(--text-grey);
    font-size: 12px;
    line-height: 1.55;
  }
  .contact__name {
    font-size: 21px;
    font-weight: 600;
    color: var(--brand-blue);
    letter-spacing: 0.5px;
    text-transform: uppercase;
    line-height: 1.1;
  }
  .contact__title { margin-bottom: 8px; }
  .contact__line { display: flex; align-items: center; gap: 6px; }
  .contact__icon { width: 10px; height: 10px; flex: none; }
</style>
</head>
<body>
<main class="stage">
  <section class="card card--front" aria-label="Business card front">
    <div class="wordmark"><span class="wordmark__dot"></span>HomeBridle</div>

    <div class="licence">
      <p>NMLS 61947</p>
      <p>Company NMLS 472815</p>
    </div>

    <div class="contact">
      <p class="contact__name">Derek Walsh</p>
      <p class="contact__title">CEO</p>
      <p>48 Birchfield Court,</p>
      <p>Suite 314, Marlow, OH 43952</p>
      <p class="contact__line">
        <svg class="contact__icon" viewBox="0 0 10 10" aria-hidden="true">
          <path d="M2 0.8 L3.6 0.8 L4.2 3 L3 3.8 Q4 6 6.2 7 L7 5.8 L9.2 6.4 L9.2 8 Q9.2 9.2 8 9.2 Q1 8.6 0.8 2 Q0.8 0.8 2 0.8 Z" fill="var(--brand-blue)"/>
        </svg>
        614-208-3917
      </p>
      <p class="contact__line">
        <svg class="contact__icon" viewBox="0 0 10 10" aria-hidden="true">
          <rect x="0.6" y="1.8" width="8.8" height="6.4" rx="0.8" fill="none" stroke="var(--brand-blue)" stroke-width="1.2"/>
          <path d="M0.8 2.2 L5 5.4 L9.2 2.2" fill="none" stroke="var(--brand-blue)" stroke-width="1.2"/>
        </svg>
        email@homebridle-example.com
      </p>
    </div>
  </section>

  <section class="card card--back" aria-label="Business card back">
    <div class="wordmark"><span class="wordmark__dot"></span>HomeBridle</div>
  </section>
</main>
</body>
</html>
```